Letterhead and Envelope Design for Investment Company

We need a letterhead and envelope design.
We are a family owned investment company doing direct investments into other family owned businesses.
I have attached all our current marketing material including our logo for reference.

Our under construction website can be found here:
https://owen-darby-qk7m.sitebrella.example/
password: Marrowdale

Target Market(s)

Bankers, business owners, financial partners

Industry/Entity Type

Investment

Colors

Designer to choose colors to be used in the design.

Requirements
Must have
• Logo, and company information

```html
<!DOCTYPE html>
<html lang="en">
<head>
<meta charset="utf-8">
<title>Marrowdale Holdings Stationery</title>
<link rel="stylesheet" href="https://fonts.googleapis.com/css2?family=Cinzel:wght@500&family=PT+Sans:wght@400&display=swap">
<style>
  :root {
    --gold: #bd8b2e;
    --ink: #231f20;
    --paper: #ffffff;
    --bg-dark: #4a4a4a;
    --bg-light: #dcdcdc;
  }
  * { margin: 0; padding: 0; box-sizing: border-box; }
  html, body { width: 1200px; height: 900px; overflow: hidden; }
  body {
    position: relative;
    background: linear-gradient(135deg, var(--bg-dark) 0%, #8d8d8d 45%, var(--bg-light) 100%);
    font-family: "PT Sans", sans-serif;
  }
  .sheet {
    position: absolute;
    background: var(--paper);
    overflow: hidden;
  }
  .sheet svg.swoosh { position: absolute; left: 0; top: 0; width: 100%; height: 100%; }
  .letterhead { left: 78px; top: 133px; width: 490px; height: 633px; }
  .envelope-front { left: 590px; top: 210px; width: 548px; height: 230px; }
  .envelope-back { left: 587px; top: 490px; width: 548px; height: 230px; }

  .company-name {
    position: absolute;
    font-family: "Cinzel", serif;
    font-weight: 500;
    color: var(--ink);
    white-space: nowrap;
    letter-spacing: 0.2px;
  }
  .letterhead .company-name { left: 44px; top: 52px; font-size: 11px; }
  .envelope-front .company-name { left: 24px; top: 40px; font-size: 10.5px; }
  .envelope-back .company-name {
    left: 0; width: 100%; top: 17px; text-align: center;
    font-size: 7.5px; color: var(--paper);
  }

  .contact {
    position: absolute;
    list-style: none;
    font-size: 6.6px;
    line-height: 1.35;
    color: var(--ink);
  }
  .letterhead .contact { left: 362px; top: 19px; }
  .envelope-front .contact { left: 24px; top: 149px; }
  .contact li { display: flex; align-items: flex-start; margin-bottom: 1.5px; }
  .contact li.address { margin-bottom: 2.5px; }
  .contact .icon { width: 6px; height: 6px; margin-right: 4px; margin-top: 1px; flex: none; fill: var(--gold); }
</style>
</head>
<body>

<section class="sheet letterhead">
  <svg class="swoosh" viewBox="0 0 490 633" preserveAspectRatio="none" aria-hidden="true">
    <path d="M0,619 L200,619 Q420,603 490,518 L490,633 L0,633 Z" fill="var(--gold)"/>
    <path d="M230,633 Q440,612 490,532 L490,633 Z" fill="var(--ink)"/>
  </svg>
  <div class="company-name">Marrowdale Holdings Inc</div>
  <ul class="contact">
    <li class="address"><svg class="icon" viewBox="0 0 10 10"><path d="M5 0 L10 5 H8.5 V10 H6 V7 H4 V10 H1.5 V5 H0 Z"/></svg><span>Marrowdale Holdings, Inc.<br>418 Harlow Ave. NE; Suite 210<br>Brookfield, MN 55912</span></li>
    <li><svg class="icon" viewBox="0 0 10 10"><rect width="10" height="10" rx="2"/></svg><span>555-204-7713</span></li>
    <li><svg class="icon" viewBox="0 0 10 10"><path d="M0 1.5 H10 V8.5 H0 Z"/></svg><span>inquiries@marrowdaleholdings.com</span></li>
    <li><svg class="icon" viewBox="0 0 10 10"><circle cx="5" cy="5" r="5"/></svg><span>marrowdaleholdings.com</span></li>
  </ul>
</section>

<section class="sheet envelope-front">
  <svg class="swoosh" viewBox="0 0 548 230" preserveAspectRatio="none" aria-hidden="true">
    <path d="M0,215 L250,215 Q480,210 548,127 L548,230 L0,230 Z" fill="var(--gold)"/>
    <path d="M330,230 Q500,214 548,140 L548,230 Z" fill="var(--ink)"/>
  </svg>
  <div class="company-name">Marrowdale Holdings Inc</div>
  <ul class="contact">
    <li class="address"><svg class="icon" viewBox="0 0 10 10"><path d="M5 0 L10 5 H8.5 V10 H6 V7 H4 V10 H1.5 V5 H0 Z"/></svg><span>Marrowdale Holdings, Inc.<br>418 Harlow Ave. NE; Suite 210<br>Brookfield, MN 55912</span></li>
    <li><svg class="icon" viewBox="0 0 10 10"><rect width="10" height="10" rx="2"/></svg><span>555-204-7713</span></li>
    <li><svg class="icon" viewBox="0 0 10 10"><path d="M0 1.5 H10 V8.5 H0 Z"/></svg><span>inquiries@marrowdaleholdings.com</span></li>
    <li><svg class="icon" viewBox="0 0 10 10"><circle cx="5" cy="5" r="5"/></svg><span>marrowdaleholdings.com</span></li>
  </ul>
</section>

<section class="sheet envelope-back">
  <svg class="swoosh" viewBox="0 0 548 230" preserveAspectRatio="none" aria-hidden="true">
    <polygon points="0,0 548,0 540,10 8,10" fill="var(--gold)"/>
    <polygon points="8,10 540,10 522,35 26,35" fill="var(--ink)"/>
  </svg>
  <div class="company-name">Marrowdale Holdings Inc</div>
</section>

</body>
</html>
```